KBS PSYCHIATRIC ASSOCIATES INC NEEDS A LOGO AND BUSINESS CARD

I am changing my business name and need a fresh logo and business card. I run a psychiatric consultation service and also provide both in-person and telehealth psychiatric care.

Janet R Farrow PhD, DNP, APRN, PMHNP-BC, RN, MSN
8315 27th AVE CT NW
Port Alder, WA 98410
318-555-0172

```html
<!DOCTYPE html>
<html lang="en">
<head>
<meta charset="utf-8">
<title>KBS Psychiatric Associates Inc – Business Card</title>
<link href="https://fonts.googleapis.com/css2?family=Cinzel:wght@400&family=Tinos:wght@400;700&display=swap" rel="stylesheet">
<style>
  :root {
    --stage: #e8e5e0;
    --paper-light: #f4f4f4;
    --paper-shade: #dcdcdc;
    --teal: #17a39e;
    --teal-deep: #12817d;
    --teal-bright: #22b5b0;
    --charcoal: #333436;
    --charcoal-deep: #2a2b2d;
    --ink-white: #ffffff;
    --ink-soft: #e9eeee;
  }
  * { box-sizing: border-box; margin: 0; padding: 0; }
  html, body {
    width: 1200px; height: 917px; overflow: hidden;
    background: var(--stage);
  }
  .canvas {
    position: relative; width: 1200px; height: 917px;
    display: flex; align-items: center; justify-content: center; gap: 50px;
  }
  .card {
    position: relative; width: 540px; height: 309px;
    border-radius: 16px; overflow: hidden;
    box-shadow: 0 10px 28px rgba(0,0,0,.22), 0 2px 6px rgba(0,0,0,.15);
  }

  /* Front */
  .card-front { background: var(--charcoal); }
  .front-top {
    position: absolute; left: 0; top: 0; width: 100%; height: 168px;
    background: linear-gradient(180deg, var(--paper-light), var(--paper-shade));
  }
  .front-band {
    position: absolute; left: 0; top: 168px; width: 100%; height: 26px;
    background: var(--teal);
    display: flex; align-items: center; gap: 14px; padding-left: 30px;
    white-space: nowrap;
  }
  .holder-name {
    font-family: "Tinos", serif; font-weight: 700; font-size: 17px;
    letter-spacing: .5px; color: var(--ink-white); text-transform: uppercase;
  }
  .holder-credentials {
    font-family: "Tinos", serif; font-size: 11.5px; color: var(--ink-white);
  }
  .front-bottom {
    position: absolute; left: 0; top: 194px; width: 100%; height: 115px;
    background: linear-gradient(180deg, var(--charcoal), var(--charcoal-deep));
    padding: 22px 0 0 30px;
  }
  .contact-row {
    display: flex; align-items: flex-start; gap: 12px;
    font-family: "Tinos", serif; font-size: 14px; line-height: 18px;
    color: var(--ink-soft); margin-bottom: 6px;
  }
  .contact-icon { width: 12px; height: 14px; margin-top: 2px; flex: none; }

  .brand {
    position: absolute; display: flex; align-items: center; gap: 18px;
    font-family: "Cinzel", serif; font-weight: 400; white-space: nowrap;
  }
  .brand-initials { font-size: 64px; line-height: 1; letter-spacing: 2px; }
  .brand-name { font-size: 21px; line-height: 26px; letter-spacing: 3px; }
  .card-front .brand { left: 70px; top: 48px; color: var(--teal); }

  /* Back */
  .card-back {
    background: radial-gradient(ellipse at 65% 35%, var(--teal-bright), var(--teal) 55%, var(--teal-deep));
  }
  .card-back .brand { left: 72px; top: 114px; color: var(--ink-white); }
</style>
</head>
<body>
<main class="canvas">

  <section class="card card-front" aria-label="Business card front">
    <div class="front-top">
      <div class="brand">
        <span class="brand-initials">KBS</span>
        <span class="brand-name">PSYCHIATRIC<br>ASSOCIATES INC</span>
      </div>
    </div>
    <div class="front-band">
      <span class="holder-name">Janet R Farrow</span>
      <span class="holder-credentials">PhD, DNP, APRN, PMHNP-BC, RN, MSN</span>
    </div>
    <div class="front-bottom">
      <div class="contact-row">
        <svg class="contact-icon" viewBox="0 0 12 14" aria-hidden="true">
          <path d="M6 0a5 5 0 0 0-5 5c0 3.6 5 9 5 9s5-5.4 5-9a5 5 0 0 0-5-5z" fill="var(--teal)"/>
          <circle cx="6" cy="5" r="1.8" fill="var(--charcoal)"/>
        </svg>
        <span>8315 27th AVE CT NW<br>Port Alder, WA 98410</span>
      </div>
      <div class="contact-row">
        <svg class="contact-icon" viewBox="0 0 12 14" aria-hidden="true">
          <path d="M3 1l2 3-1.3 1.2c.7 1.8 1.8 3 3.3 3.9L8.2 7.8l3 2-1 2.6C6 12.6 1.4 8 1 2.2z" fill="var(--teal)"/>
        </svg>
        <span>318-555-0172</span>
      </div>
    </div>
  </section>

  <section class="card card-back" aria-label="Business card back">
    <div class="brand">
      <span class="brand-initials">KBS</span>
      <span class="brand-name">PSYCHIATRIC<br>ASSOCIATES INC</span>
    </div>
  </section>

</main>
</body>
</html>
```